Classy, Elegant, Simple Business Card Design

Looking to have a classy, simple, and elegant design. Want a top notch designed business card. I really like the look of the new brivo credit card. I also like the design I attached. I am trying to reach 21-29 year old females for booking us for there wedding or event. We offer Disc Jockey Service, Photo Booth Rentals, and Uplighting .

Target Market(s)

21-28 year old females

Contact Information for Business Card

Has to have logo, website, email, and phone number

Font styles to use
Other font styles liked:
• open to font choice, modern, clean
Designer to choose
33a6d7
0791cd
0555a3
ffffff

Requirements
Must have
• Has to have logo, website, email, and phone number
Nice to have
• I really like the design of the new brivo credit card. I also included my logo and some designs I like
Should not have
• clutter or too much info

```html
<!DOCTYPE html>
<html lang="en">
<head>
<meta charset="utf-8">
<title>Echoline Event Group — Business Card</title>
<link rel="stylesheet" href="https://fonts.googleapis.com/css2?family=Montserrat:wght@300;500;700&display=swap">
<style>
  :root {
    --backdrop: #ecebea;
    --card: #ffffff;
    --navy: #0555a3;
    --blue: #0791cd;
    --sky: #33a6d7;
    --muted: #8a8d92;
  }
  html, body {
    margin: 0;
    width: 1200px;
    height: 1200px;
    overflow: hidden;
    background: var(--backdrop);
  }
  .stage {
    width: 1200px;
    height: 1200px;
    display: flex;
    align-items: center;
    justify-content: center;
  }
  .business-card {
    position: relative;
    width: 1000px;
    height: 560px;
    background: var(--card);
    overflow: hidden;
    font-family: "Montserrat", sans-serif;
    box-shadow: 0 2px 10px rgba(0,0,0,0.08);
  }
  .brand-block {
    position: absolute;
    top: 170px;
    left: 0;
    right: 0;
    text-align: center;
  }
  .brand-name {
    display: inline-flex;
    align-items: center;
    gap: 14px;
    font-weight: 500;
    font-size: 46px;
    letter-spacing: 2px;
    color: var(--navy);
    margin: 0;
  }
  .brand-dot {
    width: 16px;
    height: 16px;
    border-radius: 50%;
    background: var(--sky);
  }
  .brand-tagline {
    margin: 8px 0 0;
    font-weight: 300;
    font-size: 17px;
    letter-spacing: 9px;
    color: var(--muted);
    text-transform: uppercase;
  }
  .wordmark-band {
    position: absolute;
    left: 0;
    bottom: 0;
    width: 1000px;
    height: 130px;
  }
  .wordmark-band text {
    font-family: "Montserrat", sans-serif;
    font-weight: 700;
    fill: var(--blue);
  }
</style>
</head>
<body>
  <main class="stage">
    <section class="business-card">
      <div class="brand-block">
        <h1 class="brand-name"><span class="brand-dot"></span>ECHOLINE</h1>
        <p class="brand-tagline">Event Group</p>
      </div>
      <svg class="wordmark-band" viewBox="0 0 1000 130" aria-hidden="true">
        <text x="6" y="196" font-size="180" textLength="1010" lengthAdjust="spacingAndGlyphs">ECHOLINE</text>
      </svg>
    </section>
  </main>
</body>
</html>
```